Einladung zum Geburtstag
Einladung zu einer Geburtstagsparty von zwei "Mädels", die zusammen 99 Jahre jung werden.
Eine wird 55 (25.8.) die andere 44. (24.8.) - alles "Schnapszahlen".
Es soll eine kleine Party tagsüber für die Arbeitskollegen werden, mit Imbiss und Umtrunk. Termin für die Feier ist der 25.8. ab 14h.
Die Einladung soll sowohl gedruckt als auch per Mail verschickt werden können.

```html
<!DOCTYPE html>
<html lang="de">
<head>
<meta charset="utf-8">
<title>Einladung zur Geburtstagsparty</title>
<link href="https://fonts.googleapis.com/css2?family=Archivo+Black&family=Noto+Sans:wght@400&display=swap" rel="stylesheet">
<style>
  :root {
    --paper: #ffffff;
    --ink: #1a1a1a;
    --swoosh-yellow: rgba(236, 232, 110, 0.75);
    --swoosh-green: rgba(150, 226, 130, 0.7);
    --swoosh-cyan: rgba(120, 222, 214, 0.65);
    --title-white: #ffffff;
    --title-pink: #d24fae;
    --title-plum: #8a2b74;
    --title-edge: #6f6f6f;
    --bloom-green: rgba(60, 190, 80, 0.55);
    --bloom-teal: rgba(40, 150, 130, 0.45);
    --bloom-gold: rgba(214, 196, 110, 0.45);
  }
  * { margin: 0; padding: 0; box-sizing: border-box; }
  html, body { width: 800px; height: 1200px; overflow: hidden; background: var(--paper); }
  .invitation {
    position: relative;
    width: 800px;
    height: 1200px;
    overflow: hidden;
    background:
      radial-gradient(ellipse 300px 420px at 150px 260px, var(--swoosh-green), transparent 70%),
      radial-gradient(ellipse 260px 240px at 330px 150px, var(--swoosh-yellow), transparent 70%),
      radial-gradient(ellipse 300px 260px at 560px 300px, var(--swoosh-cyan), transparent 70%),
      var(--paper);
  }
  .backdrop { position: absolute; inset: 0; }
  .floral-right, .floral-left {
    position: absolute;
  }
  .floral-right {
    left: 380px; top: 270px; width: 420px; height: 930px;
    background:
      radial-gradient(ellipse 200px 260px at 300px 160px, var(--bloom-green), transparent 70%),
      radial-gradient(ellipse 220px 300px at 220px 720px, var(--bloom-teal), transparent 70%),
      radial-gradient(ellipse 180px 200px at 120px 480px, rgba(80,200,100,0.3), transparent 70%);
  }
  .floral-left {
    left: 0; top: 740px; width: 420px; height: 460px;
    background:
      radial-gradient(ellipse 200px 180px at 110px 220px, var(--bloom-gold), transparent 72%),
      radial-gradient(ellipse 180px 160px at 300px 140px, rgba(200,220,150,0.35), transparent 72%);
  }
  .title {
    position: absolute;
    top: 168px; left: 0; width: 800px;
    text-align: center;
    font-family: "Archivo Black", sans-serif;
    font-size: 76px;
    line-height: 1;
    letter-spacing: -1px;
    background: linear-gradient(90deg, var(--title-white) 0%, var(--title-white) 22%, var(--title-pink) 45%, var(--title-plum) 70%, var(--title-pink) 100%);
    -webkit-background-clip: text;
    background-clip: text;
    color: transparent;
    filter:
      drop-shadow(1px 1px 0 var(--title-edge))
      drop-shadow(2px 2px 0 var(--title-edge))
      drop-shadow(2px 3px 0 #4a4a4a)
      drop-shadow(3px 4px 3px rgba(0,0,0,0.35));
  }
  .poem, .details {
    position: absolute;
    left: 0; width: 800px;
    text-align: center;
    font-family: "Noto Sans", sans-serif;
    font-size: 20px;
    line-height: 29px;
    color: var(--ink);
  }
  .poem { top: 388px; }
  .poem .stanza { margin-bottom: 58px; }
  .details { top: 893px; }
</style>
</head>
<body>
<main class="invitation">
  <svg class="backdrop" width="800" height="1200" viewBox="0 0 800 1200" aria-hidden="true">
    <path d="M0 420 C 160 260, 380 160, 800 120" fill="none" stroke="rgba(255,255,255,0.8)" stroke-width="6"/>
    <path d="M0 520 C 200 360, 420 260, 800 260" fill="none" stroke="rgba(255,255,255,0.6)" stroke-width="4"/>
    <path d="M40 0 C 120 200, 260 320, 520 380" fill="none" stroke="rgba(255,255,255,0.5)" stroke-width="3"/>
  </svg>
  <div class="floral-right" role="img" aria-label="Gezeichnete Blumenranken in Grün und Türkis"></div>
  <div class="floral-left" role="img" aria-label="Zarte Blumenranken in Gold und hellem Grün"></div>

  <h1 class="title">Geburtstagsparty</h1>

  <section class="poem">
    <p class="stanza">Unaufhaltsam still und leise<br>mehren sich die Jahreskreise.</p>
    <p class="stanza">Wer älter wird der staunt darüber,<br>wie alles ging so schnell vorüber.</p>
    <p class="stanza">Plötzlich macht im Gang der Zeit eine<br>runde Zahl sich breit.</p>
    <p class="stanza">Die neue Zahl, die lässt mich kalt,<br>man ist, wie man sich fühlt so alt.</p>
  </section>

  <p class="details">Wir laden zum Prosecco ein am 25.08.2011.<br>Um 14 Uhr wird ausgeschenkt.</p>
</main>
</body>
</html>
```